Stationery Refresh For Local Mortgage Broker

We want to modernise and standardise our stationery, including: letterhead, presentation folder, email signature and business card.

The new stationery should be a more modern and professional take on our existing colour scheme and brand. (We do not want a complete overhaul.) A folder of approved stock photos can be found here: https://filebox.example-share.net/f/7kQzR2mTn4vWx9Lp3Yb8-HsdJe5Uc1Ga/view

Our current website is: www.brindlecovefin.com.au but we will be updating this to be consistent with our new stationery.

We are open to *very slight* tweaks to our logo if you feel it needs modernising, but overall we would like to maintain consistent colour scheme.

> Letterhead

148 Calloway Parade,
Geelong, VIC, 3220
ABN: 31 805 249 067
Australian Credit License: 718293

(03) 5391 6084
www.brindlecovefin.com.au

> Presentation Folder

148 Calloway Parade,
Geelong, VIC, 3220
(03) 5391 6084
www.brindlecovefin.com.au

ABN: 31 805 249 067

> Email Signature

Liam Tresidder
Director
M. 0412 857 294
P. (03) 5391 6084
www.brindlecovefin.com.au
148 Calloway Parade,
Geelong, VIC, 3220

ABN: 31 805 249 067

(you can also include a photo if you like: https://brindlecovefin.com.au/wp-content/uploads/2020/12/Liam-Tresidder.png.webp)

> Business Card

Liam Tresidder
Director
M. 0412 857 294
P. (03) 5391 6084
www.brindlecovefin.com.au
148 Calloway Parade,
Geelong, VIC, 3220

ABN: 31 805 249 067

Additional information...

If it's useful/relevant, the services we offer are: Home Loans, Investment Loans, Refinance, Debt Consolidation, Commercial Finance, Vehicle Loans
(You may choose to use this in any of the designs)

Target Market(s)

Home Buyers and Investors

Industry/Entity Type

Mortgage broking/property/real estate

Requirements
Must have
• At least somewhat consistent with our current site (yet meaningfully modernized)
Should not have
• dramatically different logo or colourscheme overhauls

```html
<!DOCTYPE html>
<html lang="en">
<head>
<meta charset="utf-8">
<title>Brindle Cove Financial Services – Business Card</title>
<link rel="stylesheet" href="https://fonts.googleapis.com/css2?family=Carlito:wght@400;700&display=swap">
<style>
  :root {
    --brand-red: #9c0910;
    --brand-grey: #666668;
    --ink-light: #ffffff;
    --stage: #ebe8e6;
    --frost-1: #f6f2f0;
    --frost-2: #ddd6d3;
    --frost-3: #c5bcba;
    --name-faint: rgba(156, 9, 16, 0.3);
  }
  * { box-sizing: border-box; margin: 0; padding: 0; }
  html, body { width: 1200px; height: 1181px; overflow: hidden; }
  body {
    background: var(--stage);
    position: relative;
    font-family: "Carlito", "Calibri", sans-serif;
    color: var(--ink-light);
  }
  .card {
    position: absolute;
    width: 654px;
    height: 403px;
    overflow: hidden;
    box-shadow: 0 6px 22px rgba(0,0,0,0.18);
  }
  .card--front {
    left: 181px; top: 156px;
    background: linear-gradient(to right, var(--brand-red) 0 470px, var(--brand-grey) 470px 100%);
  }
  .card--back {
    left: 480px; top: 627px;
    background: linear-gradient(to right, var(--brand-grey) 0 200px, var(--brand-red) 200px 100%);
  }
  .frost-window {
    position: absolute;
    width: 326px; height: 326px;
    border-radius: 50%;
    background: radial-gradient(circle at 50% 60%, var(--frost-1) 0%, var(--frost-2) 62%, var(--frost-3) 100%);
    display: flex;
    align-items: center;
    justify-content: center;
  }
  .card--front .frost-window { left: 301px; top: 39px; }
  .card--back .frost-window { left: 43px; top: 38px; }

  .company-name {
    font-family: "Carlito", "Calibri", sans-serif;
    font-weight: 700;
    font-size: 24px;
    line-height: 1.2;
    text-align: center;
    color: var(--brand-red);
    margin-top: -10px;
  }
  .card--back .company-name { color: var(--name-faint); }

  .holder { position: absolute; left: 30px; top: 56px; }
  .holder__name { font-size: 27px; font-weight: 700; line-height: 1; letter-spacing: 0.01em; }
  .holder__role { font-size: 15px; line-height: 1; margin-top: 6px; }

  .address { position: absolute; left: 30px; top: 140px; font-size: 18px; line-height: 24px; }

  .contacts { position: absolute; left: 30px; top: 218px; list-style: none; font-size: 18px; }
  .contacts li { display: flex; align-items: center; height: 24px; }
  .contacts svg { width: 16px; height: 16px; margin-right: 8px; flex: none; }

  .registration { position: absolute; left: 31px; top: 321px; font-size: 18px; line-height: 24px; }

  .services {
    position: absolute;
    right: 48px; top: 114px;
    list-style: none;
    text-align: right;
    font-size: 18px;
    text-transform: uppercase;
  }
  .services li { height: 29.5px; line-height: 29.5px; display: flex; justify-content: flex-end; align-items: center; }
  .services li::after {
    content: "";
    width: 9px; height: 9px;
    border-radius: 50%;
    background: var(--ink-light);
    margin-left: 7px;
  }
</style>
</head>
<body>

<section class="card card--front" aria-label="Business card front">
  <div class="holder">
    <p class="holder__name">LIAM TRESIDDER</p>
    <p class="holder__role">DIRECTOR</p>
  </div>

  <p class="address">148 Calloway Parade<br>Geelong, VIC, 3220</p>

  <ul class="contacts">
    <li>
      <svg viewBox="0 0 16 16" aria-hidden="true"><path d="M4 1.5l2.2 3-1.3 1.6c.8 1.8 2.2 3.2 4 4l1.6-1.3 3 2.2-1.2 2.5c-5.5-.3-10-4.8-10.3-10.3z" fill="none" stroke="#fff" stroke-width="1.5" stroke-linejoin="round"/><path d="M9.5 1.8a5 5 0 0 1 4.7 4.7M9.3 4.3a2.6 2.6 0 0 1 2.4 2.4" fill="none" stroke="#fff" stroke-width="1.3" stroke-linecap="round"/></svg>
      0412 857 294
    </li>
    <li>
      <svg viewBox="0 0 16 16" aria-hidden="true"><rect x="3.5" y="1" width="9" height="14" rx="1.5" fill="none" stroke="#fff" stroke-width="1.6"/><line x1="6.5" y1="12.5" x2="9.5" y2="12.5" stroke="#fff" stroke-width="1.4"/></svg>
      (03) 5391 6084
    </li>
    <li>
      <svg viewBox="0 0 16 16" aria-hidden="true"><g fill="none" stroke="#fff" stroke-width="1.2"><circle cx="8" cy="8" r="6.8"/><ellipse cx="8" cy="8" rx="3" ry="6.8"/><line x1="1.2" y1="8" x2="14.8" y2="8"/><path d="M2.2 4.6h11.6M2.2 11.4h11.6"/></g></svg>
      www.brindlecovefin.com.au
    </li>
  </ul>

  <p class="registration">ABN: 31 805 249 067<br>Australian Credit License: 718293</p>

  <div class="frost-window">
    <p class="company-name">Brindle Cove<br>Financial Services</p>
  </div>
</section>

<section class="card card--back" aria-label="Business card back">
  <div class="frost-window">
    <p class="company-name">Brindle Cove<br>Financial Services</p>
  </div>

  <ul class="services">
    <li>Home Loans</li>
    <li>Investment Loans</li>
    <li>Refinance</li>
    <li>Debt Consolidation</li>
    <li>Commercial Finance</li>
    <li>Vehicle Loans</li>
  </ul>
</section>

</body>
</html>
```